Velvet Comet Gummy Bottle Label

****UPDATED PROJECT BRIEF & UPDATED PROJECT DOC ATTACHED INCLUDING A LOGO DESIGN WE LIKE AND EXAMPLE LABELS WE LIKE****
(see attached word doc for full project description)
Brand Name:
Velvet Comet
Project Overview:
Velvet Comet is a trippy blend of psychoactive organic mushrooms, functional mushrooms, vitamins and designer cannabinoids all contained in a delicious gummy supplement that enhances your reality. This brand’s identity is trippy, psychedelic, fun and escapism. The Velvet Comet label will be placed on gummy bottles and gummy bags that will be sold online through an ecommerce webpage, social media campaigns and on shelves in retail stores.
Label Request:
The Velvet Comet products are gummies that will be placed in bottles and/or bags. There will be 6 different products with designated moods and flavors (i.e. Sleep/Lavender Vanilla, Calm/blackberry, Uplift/Pineapple, Focus/peach, Defense/black cherry, Energy/orange).
Dimensions will vary, here are a few:
Bottles:
6" W x 2" H
5" W x 2" H
Pouches:
4 x 6 x 2"
Label elements we like:
Label should be fun to look at sober, and trippy (a blast) to look at after you've taken the product
Label should invoke a mushroom effect. Examples of “the mushroom effect” below:
Mostly it’s just glowing colors, distortions, details popping out…good vibes
an explosion of stimuli, my mind zipped through so many connections
Your sense of time and space perception will be warped
colors appear to glow
You’ll notice surfaces glittering and an increased richness in texture of (all) things.
You may find yourself smiling uncontrollably, or feeling especially giggly.
First feelings are usually those of euphoria and an "opening up" of the world where colors become more vivid and solid objects appear to "breathe."
Product Information:
Uplifting
Flavor: Pineapple
Product Name: Uplift
Effects: Mood Enhancement, Mental Health Helper
Front Label Ingredients: Amanita & Cordyceps
Back Label Ingredients: Magnesium, Vit B2 Riboflavin, Vitamin B6 Pyridoxine, Ginkgo, Theacrine, Rhodiola Rosea, Shiitake, Cordyceps, Myrcene, Pinene, Amanita, D10, THCV,
Focus
Flavor: Sunny Dazzle
Product Name: Focus
Effects: Focused, Creative, Productive
Label Ingredients: Lions Mane & Cordyceps
Back Label Ingredients: Rhodiola Rosea, L-theanine, Luteolin, Forskolin, Ginkgo, Lions Mane, Cordyceps, Pinene, Caryphyllene, Amanita, D10
Defense
Flavor: Black Cherry
Product Name: Defend
Effects: Immunity & Gut Health
Label Ingredients: Turkey Tail & Ashwagandha
Back Label Ingredients: Ashwagandha, Resveratrol, Vit A, Vit C, Ginger, Magnesium Glycinate, Lemon Balm, Maitake, Turkey Tail, Lions Mane, Caryophyllene, Limonene, Humulene, Amanita, CBG, CBC.
Energy
Flavor: Tangy Tornado
Product Name: Energy
Effects: Awake, Stamina, Active
Back Label Ingredients: Choline, Coluracetam, Caffeine, Vitamin B1 Thiamin, B3 Niacin, L-theanine, Creatine, Rhodiola Rosea, Ginkgo, Cordyceps, Lions Mane, Limonene, Valencene, Amanita, D10
Sleep
Flavor: Vanilla Lavender
Product Name: Sleep
Effects: Bedtime, Naptime, Relax Time
Label Ingredients: Melatonin & Reishi
Back Label Ingredients: Melatonin, Ashwagandha, Reishi, Bobinsana, Passion Flower, Linalool.
Calm
Flavor: Plum Parade
Product Name: Calm
Effects: Chill, Relaxed, Good Vibes
Label Ingredients: Amanita & Reishi
Back Label Ingredients: Ashwagandha, Lemon Balm, Reishi, Chamomile, Velvet Bean, Caryophyllene, Amanita, D8, HHC
Psychedelic Mushrooms

```html
<!DOCTYPE html>
<html lang="en">
<head>
<meta charset="utf-8">
<title>Velvet Comet – Energy Gummies Label</title>
<link href="https://fonts.googleapis.com/css2?family=Open+Sans:wght@400;600;700&display=swap" rel="stylesheet">
<style>
  :root {
    --page-bg: #ecebe9;
    --label-red: #d9262b;
    --label-ink: #1f1f1f;
    --swirl-pink: #e98fd0;
    --swirl-yellow: #f1ec4e;
    --swirl-orange: #f0a94a;
    --swirl-cream: #f7f0ef;
  }
  * { box-sizing: border-box; margin: 0; padding: 0; }
  html, body {
    width: 1200px;
    height: 1200px;
    overflow: hidden;
    background: var(--page-bg);
    font-family: "Open Sans", sans-serif;
  }
  .label {
    position: absolute;
    left: 220px;
    top: 120px;
    width: 760px;
    height: 960px;
    overflow: hidden;
  }
  .label-pattern {
    position: absolute;
    inset: 0;
    background:
      radial-gradient(circle at 20% 15%, var(--swirl-yellow) 0, transparent 30%),
      radial-gradient(circle at 80% 25%, var(--swirl-pink) 0, transparent 32%),
      radial-gradient(circle at 30% 70%, var(--swirl-orange) 0, transparent 35%),
      radial-gradient(circle at 75% 85%, var(--swirl-yellow) 0, transparent 30%),
      radial-gradient(circle at 10% 95%, var(--swirl-pink) 0, transparent 28%),
      var(--swirl-cream);
  }
  .label-copy {
    position: absolute;
    inset: 0;
    text-align: center;
    color: var(--label-red);
  }
  .product-title {
    position: absolute;
    top: 215px;
    left: 0;
    right: 0;
    font-size: 100px;
    font-weight: 400;
    line-height: 0.98;
    letter-spacing: -1px;
  }
  .mood {
    position: absolute;
    top: 500px;
    left: 0;
    right: 0;
    font-size: 76px;
    font-weight: 400;
    line-height: 1;
  }
  .flavor {
    position: absolute;
    top: 588px;
    left: 0;
    right: 0;
    font-size: 50px;
    font-weight: 400;
    line-height: 1;
    letter-spacing: -0.5px;
  }
  .effects {
    position: absolute;
    top: 646px;
    left: 0;
    right: 0;
    font-size: 22px;
    color: var(--label-ink);
    letter-spacing: 0.3px;
  }
  .count {
    position: absolute;
    top: 740px;
    left: 0;
    right: 0;
    font-size: 36px;
    font-weight: 700;
    color: var(--label-ink);
  }
  .dose {
    position: absolute;
    top: 792px;
    left: 0;
    right: 0;
    font-size: 26px;
    color: var(--label-ink);
  }
  .net-weight {
    position: absolute;
    top: 858px;
    left: 0;
    right: 0;
    font-size: 18px;
    color: var(--label-ink);
  }
</style>
</head>
<body>
  <section class="label">
    <div class="label-pattern" role="img" aria-label="Psychedelic swirl pattern in pink, yellow and orange with line-drawn mushrooms"></div>
    <div class="label-copy">
      <h1 class="product-title">MUSHROOM<br>GUMMIES</h1>
      <p class="mood">ENERGY</p>
      <p class="flavor">TANGY TORNADO</p>
      <p class="effects">FOCUSED, CREATIVE, PRODUCTIVE</p>
      <p class="count">30 GUMMIES</p>
      <p class="dose">2500mg per gummy**</p>
      <p class="net-weight">Net Wt = 4.76 oz (136g)</p>
    </div>
  </section>
</body>
</html>
```